Business Card and Letterhead Design for Public Accounting Firm

Business card and letterhead design for a CPA Firm located in Orange County, CA. We're looking for a modern and professional design utilizing our existing logo. We'd like a clean "less is more" look, but also something that catches the eye. We provide a high level of service to our clients. Open to single or double sided business cards.

Additional info: color numbers on logo
Blue :
R 0
G 83
B 125

#00537D

Silver :

R 154
G 154
B 154

#9A9A9A

Target Market(s)

Businesses and individuals

Industry/Entity Type

Accounting

Contact Information for Business Card

Moss Whitfield & Danby LLP - 4827 Larkspur Vale Road, Irvine, CA 92614 - (949)731-2864 - mwdaccts.example

Font styles to use
Serif
Sans Serif
Other font styles liked:
• See font file uploaded

Colors
0054AA
0677BA
7BADD7
CADEEF
E8F1F8

Requirements
Nice to have
• Possibly use the font file provided which matches our logo, but adjust to be not in all caps

```html
<!DOCTYPE html>
<html lang="en">
<head>
<meta charset="utf-8">
<title>Moss Whitfield &amp; Danby LLP — Stationery</title>
<link href="https://fonts.googleapis.com/css2?family=Cinzel:wght@400;500&family=Lato:wght@400;700&family=Parisienne&display=swap" rel="stylesheet">
<style>
  :root {
    --backdrop: #2e7a72;
    --paper: #f8f7f7;
    --card: #f7f8fa;
    --brand-blue: #00537d;
    --brand-silver: #9a9a9a;
    --ink: #2b2b2b;
    --ink-soft: #3d3d3d;
  }
  * { margin: 0; padding: 0; box-sizing: border-box; }
  html, body { width: 1200px; height: 900px; overflow: hidden; }
  body { background: var(--backdrop); position: relative; font-family: "Lato", sans-serif; }

  .letterhead {
    position: absolute; left: 248px; top: 129px; width: 450px; height: 636px;
    background: var(--paper); box-shadow: 0 4px 12px rgba(0,0,0,.25);
  }
  .wordmark { display: flex; align-items: center; gap: 7px; font-family: "Cinzel", serif; color: var(--brand-blue); font-weight: 500; }
  .wordmark .mark-square { width: 14px; height: 14px; background: var(--brand-blue); flex: none; }
  .wordmark .name { letter-spacing: .08em; line-height: 1.25; }
  .letterhead .wordmark { position: absolute; left: 34px; top: 40px; }
  .letterhead .wordmark .name { font-size: 10px; }

  .letter-contact { position: absolute; left: 313px; top: 27px; font-family: "Cinzel", serif; font-size: 7px; color: var(--ink-soft); line-height: 10.8px; }
  .letter-contact .icon-row { display: flex; align-items: center; gap: 4px; margin-top: 2px; }
  .letter-contact .address { margin-bottom: 4px; }
  .icon { width: 8px; height: 8px; flex: none; }

  .letter-body { position: absolute; left: 34px; right: 34px; top: 140px; font-size: 8.6px; color: var(--ink); line-height: 10.3px; }
  .letter-body .date { margin-bottom: 11px; }
  .letter-body .block { margin-bottom: 10px; }
  .letter-body .salutation { font-size: 10.6px; font-weight: 700; margin: 4px 0 10px; }
  .letter-body p.para { text-align: justify; margin-bottom: 9px; }
  .letter-body .closing { margin-top: 22px; }
  .letter-body .signature { font-family: "Parisienne", cursive; font-size: 20px; margin-top: 12px; margin-left: 2px; color: #222; }

  .card { position: absolute; left: 726px; width: 306px; height: 176px; box-shadow: 0 4px 10px rgba(0,0,0,.3); }
  .card-front { top: 387px; background: var(--card); }
  .card-back { top: 590px; background: var(--brand-blue); display: flex; align-items: center; justify-content: center; }
  .card-front .wordmark { position: absolute; left: 0; right: 0; top: 40px; justify-content: center; }
  .card-front .wordmark .name { font-size: 10px; }
  .card-back .wordmark { color: #fff; }
  .card-back .wordmark .mark-square { background: #fff; }
  .card-back .wordmark .name { font-size: 11.5px; }

  .holder { position: absolute; left: 0; right: 0; top: 83px; text-align: center; font-family: "Cinzel", serif; }
  .holder .person { color: var(--brand-blue); font-size: 11.5px; letter-spacing: .02em; }
  .holder .role { color: var(--ink-soft); font-size: 8.5px; }
  .holder .sep { color: var(--ink-soft); font-size: 9px; margin: 0 3px; }

  .card-details { position: absolute; top: 105px; left: 0; right: 0; display: flex; justify-content: center; font-family: "Cinzel", serif; font-size: 7.4px; color: var(--ink-soft); line-height: 12.5px; }
  .card-details .office { text-align: right; padding-right: 6px; border-right: 1px solid var(--brand-blue); }
  .card-details .lines { padding-left: 6px; }
  .card-details .icon-row { display: flex; align-items: center; gap: 4px; }
</style>
</head>
<body>

<section class="letterhead">
  <div class="wordmark">
    <span class="mark-square"></span>
    <span class="name">Moss Whitfield<br>&amp; Danby LLP</span>
  </div>

  <address class="letter-contact" style="font-style:normal">
    <div class="address">Moss Whitfield &amp; Danby LLP<br>4827 Larkspur Vale Road<br>Irvine, CA 92614</div>
    <div class="icon-row">
      <svg class="icon" viewBox="0 0 10 10"><circle cx="5" cy="5" r="4.5" fill="none" stroke="#00537d" stroke-width="1"/><path d="M3 3.2h4v1H3zM2.8 4.6h4.4v2.4H2.8z" fill="#00537d"/></svg>
      <span>(949) 731-2864</span>
    </div>
    <div class="icon-row">
      <svg class="icon" viewBox="0 0 10 10"><circle cx="5" cy="5" r="4.5" fill="none" stroke="#00537d" stroke-width="1"/><circle cx="5" cy="5" r="2.6" fill="#00537d"/></svg>
      <span>www.mwdaccts.example</span>
    </div>
  </address>

  <div class="letter-body">
    <div class="date">Feb-03-2022</div>
    <div class="block">Mr, Alan Porter<br>President</div>
    <div class="block">Harbor Row Corporation<br>123 Street Name, Suite# 10<br>City, State, 120023</div>
    <div class="salutation">Dear Mr, Alan</div>
    <p class="para">Lorem ipsum dolor sit amet, consectetur adipisicing elit, sed do eiusmod tempor incididunt ut labore et dolore magna aliqua. Ut enim ad minim veniam, quis nostrud exercitation ullamco laboris nisi ut aliquip ex ea commodo consequat. Duis aute irure dolor in reprehenderit in voluptate velit esse cillum dolore eu fugiat nulla pariatur.</p>
    <p class="para">Lorem ipsum dolor sit amet, consectetur adipisicing elit, sed do eiusmod tempor incididunt ut labore et dolore magna aliqua. Ut enim ad minim veniam, quis nostrud exercitation ullamco laboris nisi ut aliquip ex ea commodo consequat. Duis aute irure dolor in reprehenderit in voluptate velit esse cillum dolore eu fugiat nulla pariatur.</p>
    <p class="para">Lorem ipsum dolor sit amet, consectetur adipisicing elit, sed do eiusmod tempor incididunt ut labore et dolore magna aliqua. Ut enim ad minim veniam, quis nostrud exercitation ullamco laboris nisi ut aliquip ex ea commodo consequat.</p>
    <p class="para">Excepteur sint occaecat cupidatat non proident, sunt in culpa qui officia deserunt mollit anim id est laborum. re et dolore magnam aliquam quaerat voluptatem.</p>
    <div class="closing">Regards</div>
    <div class="signature">Daniel Brooks</div>
  </div>
</section>

<section class="card card-front">
  <div class="wordmark">
    <span class="mark-square"></span>
    <span class="name">Moss Whitfield<br>&amp; Danby LLP</span>
  </div>
  <div class="holder">
    <span class="person">REID HALLOWAY</span><span class="sep">|</span><span class="role">Co-Founder</span>
  </div>
  <div class="card-details">
    <div class="office">Moss Whitfield &amp; Danby LLP<br>4827 Larkspur Vale<br>Road, Irvine, CA 92614</div>
    <div class="lines">
      <div class="icon-row">
        <svg class="icon" viewBox="0 0 10 10"><circle cx="5" cy="5" r="4.5" fill="none" stroke="#00537d" stroke-width="1"/><path d="M3 3.2h4v1H3zM2.8 4.6h4.4v2.4H2.8z" fill="#00537d"/></svg>
        <span>(949) 731-2864</span>
      </div>
      <div class="icon-row">
        <svg class="icon" viewBox="0 0 10 10"><circle cx="5" cy="5" r="4.5" fill="none" stroke="#00537d" stroke-width="1"/><rect x="2.8" y="3.4" width="4.4" height="3.4" fill="#00537d"/></svg>
        <span>(949) 731-2865</span>
      </div>
      <div class="icon-row">
        <svg class="icon" viewBox="0 0 10 10"><circle cx="5" cy="5" r="4.5" fill="none" stroke="#00537d" stroke-width="1"/><circle cx="5" cy="5" r="2.6" fill="#00537d"/></svg>
        <span>office@mwdaccts.example</span>
      </div>
    </div>
  </div>
</section>

<section class="card card-back">
  <div class="wordmark">
    <span class="mark-square"></span>
    <span class="name">Moss Whitfield<br>&amp; Danby LLP</span>
  </div>
</section>

</body>
</html>
```